All About How Do Title Loans Work?*

Hi There,<br/>We: Bluefern Auto Pledge Lending (Loan agency in the US) are looking to get infographic design services for our most comprehensive guide: How do Title Loans Work. <br/>This guide has 6 steps that describe the title loan process/ service that we offer to our clients. <br/>If you’d like to know how car title loans work, then read this: https://bluefernlending.example/how-do-title-loans-work/

Target Market(s)

Personal Loans in US

Industry/Entity Type

Financial

Requirements
Must have
• Logo
• 1-6 steps
• Apply now + How Much Cash Can I Get https://snapvue.example/k8tzq1 / https://snapvue.example/k8tzw4 (call to action): Find that buttons here: https://bluefernlending.example/can-i-get-a-title-loan-if-the-title-is-not-in-my-name/
• The disclaimers: Please use the disclaimer that appears below the content: examples: https://snapvue.example/k8vb37 https://snapvue.example/k8vb5n https://snapvue.example/k8vb9d etc.
Nice to have
• Marisol: https://bluefernlending.example/apply-now/ (our presenter)-> https://snapvue.example/k8tyh2
Should not have
• Colors that not related to our website
• Don't promise anything we can't deliver (we have strict guidelines in the loan industry)

```html
<!DOCTYPE html>
<html lang="en">
<head>
<meta charset="utf-8">
<title>How Do Title Loans Work – Bluefern Auto Pledge Lending</title>
<link href="https://fonts.googleapis.com/css2?family=Montserrat:wght@600;700;800&family=Open+Sans:wght@400;600&family=Saira:wght@500&display=swap" rel="stylesheet">
<style>
:root{
  --yellow:#f9c80e;
  --ink:#111111;
  --text:#222222;
  --muted:#444444;
  --dash:#333333;
  --ring:#8a8a8a;
  --footer:#f0f0f0;
  --white:#ffffff;
}
*{margin:0;padding:0;box-sizing:border-box}
html,body{width:837px;height:1200px;overflow:hidden;background:var(--white)}
.infographic{position:relative;width:837px;height:1200px;font-family:"Montserrat",sans-serif;color:var(--ink)}
.route{position:absolute;inset:0;width:837px;height:1200px}
.abs{position:absolute;white-space:nowrap}
.brand{left:0;width:837px;top:66px;display:flex;justify-content:center;align-items:center;gap:10px}
.brand-dot{width:22px;height:22px;border-radius:50%;background:var(--yellow)}
.brand-name{font-weight:700;font-size:21px;color:var(--ink);letter-spacing:.2px}
.headline{left:0;width:837px;top:165px;text-align:center;font-weight:800;font-size:20.5px;letter-spacing:.1px}
.step-title{font-weight:700;font-size:14.5px;letter-spacing:.2px}
.step-title.sm{font-size:13px}
.badge{display:inline-flex;align-items:center;justify-content:center;width:23px;height:23px;border-radius:50%;background:var(--yellow);font-weight:700;font-size:11.5px;color:var(--ink);flex:none}
.badge.lg{width:26px;height:26px;font-size:12px}
.item{display:flex;align-items:center;gap:5px;font-weight:700;font-size:7.6px;line-height:1.35}
.item.md{font-size:8.7px;gap:6px}
.item.lg{font-size:8.8px;gap:7px}
.checklist{list-style:none;font-family:"Open Sans",sans-serif;font-size:8.8px;color:var(--text)}
.checklist li{position:absolute;left:0;white-space:nowrap}
.subhead{font-weight:700;font-size:10.6px;line-height:18px}
.subhead.sm{font-size:8.5px}
.fine{font-family:"Open Sans",sans-serif;font-size:7.6px;line-height:13.4px;color:var(--text)}
.body{font-family:"Open Sans",sans-serif;font-size:10.3px;line-height:14.6px;color:var(--text)}
.disclaimers{position:absolute;left:0;top:1060px;width:837px;height:140px;background:var(--footer);padding-top:31px;text-align:center;font-family:"Open Sans",sans-serif;font-size:8.8px;line-height:13.4px;color:var(--muted)}
</style>
</head>
<body>
<main class="infographic">

<svg class="route" viewBox="0 0 837 1200" aria-hidden="true">
  <path d="M0 137H837V216H500C450 216 422 238 418 267C414 238 386 216 336 216H0Z" fill="var(--yellow)"/>
  <g fill="none" stroke="var(--dash)" stroke-width="0.8" stroke-dasharray="3 2.5">
    <path d="M166 321H445"/>
    <path d="M525 321H675C760 321 808 380 808 456C808 540 760 605 675 605H535"/>
    <path d="M166 605H447"/>
    <path d="M85 615C42 640 22 690 22 735C22 790 60 825 107 833"/>
    <path d="M188 838H440"/>
  </g>
  <g fill="none" stroke="var(--ring)" stroke-width="1.4" stroke-dasharray="0.1 3.4" stroke-linecap="round">
    <circle cx="124" cy="319" r="36"/>
    <circle cx="486" cy="319" r="36"/>
    <circle cx="124" cy="605" r="36"/>
    <circle cx="489" cy="605" r="36"/>
    <circle cx="145" cy="840" r="36"/>
    <circle cx="480" cy="840" r="36"/>
  </g>
  <g fill="var(--yellow)">
    <circle cx="300" cy="321" r="5.5"/>
    <circle cx="808" cy="456" r="5.5"/>
    <circle cx="318" cy="604" r="5.5"/>
    <circle cx="22" cy="735" r="5.5"/>
    <circle cx="318" cy="834" r="5.5"/>
  </g>
  <g font-family="Saira, sans-serif" font-size="58" font-weight="500" fill="none" stroke="var(--ink)" stroke-width="1.5" text-anchor="middle">
    <text x="125" y="339">1</text>
    <text x="487" y="339">2</text>
    <text x="125" y="625">3</text>
    <text x="487" y="627">4</text>
    <text x="147" y="860">5</text>
    <text x="480" y="860">6</text>
  </g>
  <g>
    <line x1="459" y1="472" x2="459" y2="534" stroke="var(--dash)" stroke-width="0.6" stroke-dasharray="2 2"/>
    <circle cx="459" cy="472" r="4.8" fill="var(--white)" stroke="var(--dash)" stroke-width="0.7"/>
    <circle cx="459" cy="472" r="3" fill="var(--yellow)"/>
    <circle cx="459" cy="493" r="3" fill="var(--yellow)"/>
    <circle cx="459" cy="514" r="3" fill="var(--yellow)"/>
    <circle cx="459" cy="535" r="3" fill="var(--yellow)"/>
  </g>
</svg>

<header>
  <div class="abs brand"><span class="brand-dot"></span><span class="brand-name">Bluefern Auto Pledge Lending</span></div>
  <h1 class="abs headline">6 SIMPLE STEPS TO GETTING CAR TITLE LOANS</h1>
</header>

<section class="step step-requirements">
  <h2 class="abs step-title sm" style="left:95px;top:382px">REQUIREMENTS</h2>
  <div class="abs item" style="left:96px;top:409px"><span class="badge">1</span>Your Personal details</div>
  <div class="abs item" style="left:96px;top:439px"><span class="badge">2</span>Your Car’s details</div>
  <div class="abs item" style="left:96px;top:469px"><span class="badge">3</span>Car title</div>
  <div class="abs item" style="left:214px;top:409px"><span class="badge">4</span>Identification</div>
  <div class="abs item" style="left:214px;top:436px"><span class="badge">5</span>Regular Income</div>
  <div class="abs item" style="left:214px;top:469px"><span class="badge">6</span>References</div>
</section>

<section class="step step-application">
  <h2 class="abs step-title" style="left:443px;top:382px">APPLICATION</h2>
  <div class="abs item md" style="left:443px;top:414px"><span class="badge lg">1</span><span>Call us:<br>(888) 555 0147</span></div>
  <div class="abs item md" style="left:551px;top:414px"><span class="badge lg">2</span><span>Visit one of<br>our branches</span></div>
  <div class="abs item md" style="left:649px;top:414px"><span class="badge lg">3</span><span>Apply online in<br>4 easy steps:</span></div>
  <ul class="abs checklist" style="left:472px;top:464px">
    <li style="top:0">Enter Your Car’s Details</li>
    <li style="top:21px">Your Personal Information</li>
    <li style="top:42px">Address, Date of Birth and SSN</li>
    <li style="top:63px">Upload Photos of Your Vehicle</li>
  </ul>
</section>

<section class="step step-approval">
  <h2 class="abs step-title" style="left:97px;top:668px">APPROVAL</h2>
  <p class="abs subhead" style="left:97px;top:697px">Title Loans Ranging from 25% to 1<br>20% of the Car’s Value</p>
  <p class="abs fine" style="left:97px;top:735px">All loan applications are subject to meeting our credit criteria, which<br>includes applicant’s ability to repay the loan.</p>
</section>

<section class="step step-funding">
  <h2 class="abs step-title" style="left:455px;top:668px">LOAN FUNDING</h2>
  <p class="abs subhead sm" style="left:456px;top:694px">Get Your Title Loan’s Money - Three Simple Ways**:</p>
  <div class="abs item lg" style="left:453px;top:718px"><span class="badge lg">1</span>Branch stores</div>
  <div class="abs item lg" style="left:550px;top:720px"><span class="badge lg">2</span>CashRelay</div>
  <div class="abs item lg" style="left:640px;top:722px"><span class="badge lg">3</span>Direct deposit</div>
</section>

<section class="step step-repayments">
  <h2 class="abs step-title" style="left:102px;top:902px">REPAYMENTS</h2>
  <div class="abs item lg" style="left:100px;top:935px"><span class="badge lg">1</span>By phone</div>
  <div class="abs item lg" style="left:226px;top:935px"><span class="badge lg">2</span>Online payments</div>
  <div class="abs item lg" style="left:101px;top:969px"><span class="badge lg">3</span>Cash payments</div>
  <div class="abs item lg" style="left:227px;top:969px"><span class="badge lg">4</span>Check or money order</div>
</section>

<section class="step step-closure">
  <h2 class="abs step-title" style="left:459px;top:901px">LOAN CLOSURE</h2>
  <p class="abs subhead" style="left:459px;top:932px">Get Your Title Returned</p>
  <p class="abs body" style="left:460px;top:953px">We will send back your title, without a lien, when you finish<br>paying back the loan. We might send a document of<br>lien-release rather than a clean title.</p>
</section>

<footer class="disclaimers">
  <p>*Disclaimer: There is a chance you’ll need to show additional documents.</p>
  <p>*After the application process is complete and the Underwriting Department has reviewed it, you may be given a conditional<br>offer. Funding time is dependent upon the availability of Bluefern Auto Pledge Lending offices and time necessary to complete your loan<br>process. After loan approval, the typical funding time ranges between 3 and 5 hours.</p>
  <p>***Certain debit and pre-paid cards are not eligible for this type of transaction.</p>
  <p>Disclaimer: A GPS tracking instrument will be installed in your vehicle, because you are using your car as collateral against a title loan.</p>
</footer>

</main>
</body>
</html>
```